Vertical flyer design to guide people to my shop

We need a vertical flyer design for a tailor shop, Marlow Stitchworks. Our shop is on the 3/F, and we need this flyer/poster to placed on the G/F street level to guide people to take the lifts upstairs. Basically to tell people that, "We are here on 3/F!"

Dimensions ratio: 80 (wide) x200 (tall)

You may use the photos and graphics from the webpages below.
http://www.marlowstitchworks.net/en/marlow-stitchworks-hong-kong-tailors-tailor-shop/

https://www.cloth-q.com/tailor/marlow-stitchworks

```html
<!DOCTYPE html>
<html lang="en">
<head>
<meta charset="utf-8">
<title>Marlow Stitchworks – We are here on 3/F</title>
<link rel="stylesheet" href="https://fonts.googleapis.com/css2?family=Oswald:wght@700&family=Tinos:wght@700&display=swap">
<style>
  :root {
    --stage: #efefef;
    --paper: #ffffff;
    --headline-red: #e8403a;
    --floor-red: #8e0f1e;
    --frame-brown: #6b3a16;
    --suit-dark: #3c3e44;
    --suit-mid: #5d6068;
    --sleeve-dark: #35302e;
    --sleeve-light: #8a8a8c;
    --gold-light: #f3d08a;
    --gold: #e0a23c;
    --copper: #c2692b;
  }
  html, body {
    margin: 0;
    padding: 0;
    width: 1200px;
    height: 1200px;
    overflow: hidden;
    background: var(--stage);
  }
  .canvas {
    display: block;
    width: 1200px;
    height: 1200px;
  }
  .poster-sheet { fill: var(--paper); }
  .chevron-frame { fill: var(--frame-brown); }
  .photo-suit { fill: url(#suitTone); }
  .photo-sleeve { fill: url(#sleeveTone); }
  .text-knockout { fill: var(--paper); }
  .headline-small {
    font-family: "Tinos", "Times New Roman", serif;
    font-weight: 700;
    fill: var(--headline-red);
  }
  .floor-mark {
    font-family: "Oswald", "Arial Narrow", sans-serif;
    font-weight: 700;
    fill: var(--floor-red);
  }
</style>
</head>
<body>
<svg class="canvas" viewBox="0 60 1500 1400" xmlns="http://www.w3.org/2000/svg" aria-label="Marlow Stitchworks direction flyer">
  <defs>
    <linearGradient id="suitTone" x1="0" y1="0" x2="1" y2="1">
      <stop offset="0" stop-color="var(--suit-mid)"/>
      <stop offset="0.6" stop-color="var(--suit-dark)"/>
      <stop offset="1" stop-color="#2c2b2c"/>
    </linearGradient>
    <linearGradient id="sleeveTone" x1="1" y1="0" x2="0" y2="1">
      <stop offset="0" stop-color="var(--sleeve-light)"/>
      <stop offset="0.45" stop-color="var(--sleeve-dark)"/>
      <stop offset="1" stop-color="#2a2624"/>
    </linearGradient>
    <linearGradient id="goldFade" x1="0" y1="0" x2="0" y2="1">
      <stop offset="0" stop-color="var(--gold-light)" stop-opacity="0"/>
      <stop offset="0.3" stop-color="var(--gold-light)" stop-opacity="0.55"/>
      <stop offset="0.7" stop-color="var(--gold)"/>
      <stop offset="1" stop-color="var(--copper)"/>
    </linearGradient>
  </defs>

  <g class="poster">
    <rect class="poster-sheet" x="475" y="18" width="557" height="1390"/>

    <rect class="gold-field" x="475" y="940" width="557" height="468" fill="url(#goldFade)"/>

    <g class="chevron-upper">
      <polygon class="chevron-frame" points="475,250 882,658 475,1065"/>
      <polygon class="photo-suit" role="img" aria-label="Photo: tailored grey check suit jacket, hands adjusting the cuff"
               points="475,292 850,658 475,1030"/>
    </g>

    <g class="chevron-lower">
      <polygon class="chevron-frame" points="475,1063 590,948 778,1137 507,1408 475,1408"/>
      <polygon class="photo-sleeve" role="img" aria-label="Photo: dark jacket sleeve with wristwatch and clasped hands"
               points="475,1092 590,977 748,1137 487,1400 475,1400"/>
    </g>

    <rect class="text-knockout" x="650" y="228" width="382" height="204"/>

    <text class="headline-small" x="558" y="122" font-size="78" textLength="248" lengthAdjust="spacingAndGlyphs">We are</text>
    <text class="headline-small" x="535" y="203" font-size="92" textLength="430" lengthAdjust="spacingAndGlyphs">HERE ON</text>
    <text class="floor-mark" x="658" y="432" font-size="262" textLength="354" lengthAdjust="spacingAndGlyphs">3/F!</text>
  </g>
</svg>
</body>
</html>
```